Large scale additive manufacturing system brochure

Project Title: ZORIL Series THERMOPLASTIC EXTRUDER– Product Catalog Design

Description:
We need a professional catalog design for our ZORIL Series extruders (ZORIL15, ZORIL20, ZORIL32), which are high-performance extrusion systems for large-scale thermoplastic 3D printing. The catalog should highlight technical specifications, key features, applications, and company profile.

Requirements:
• Clean and modern layout aligned with Brimtel corporate colors
• 10–12 pages including cover, product comparison tables, technical details, and application visuals
• Output capacities should be presented based on PETG +30% GF benchmark
• Integration of company’s partnerships (TOLMI, OBRU, Qe Forge, Movrel)
• Space for product renders, real application images, and technical drawings
• English text will be provided, but layout and professional design are required

Deliverables:
• Editable source file (InDesign / Illustrator / similar)
• Print-ready PDF version

*i upload the previous catalog, which doesn’t show our vision abd future aim. We need a professional, unique and impressive design.

Target Market(s)

Defense, aerospace, marine, furniture, composite manufacturing

Industry/Entity Type

Robotics and automation

Font styles to use
Sans Serif

Colors

Designer to choose colors to be used in the design.

Requirements
Must have
• High tech impressive view
Nice to have
• Must seen a unique high tech product catalog

```html
<!DOCTYPE html>
<html lang="en">
<head>
<meta charset="utf-8">
<title>ZORIL32 – Thermoplastic Extruder</title>
<link href="https://fonts.googleapis.com/css2?family=Roboto:wght@400;500;700&display=swap" rel="stylesheet">
<style>
  :root {
    --orange: #e08a2e;
    --slate: #7488a7;
    --slate-dark: #647a9c;
    --sky-top: #abcade;
    --sky-mid: #4b93b5;
    --sky-bottom: #9fc2d9;
    --ink: #111820;
    --white: #ffffff;
    --hex-edge: #1c2a38;
  }
  * { margin: 0; padding: 0; box-sizing: border-box; }
  html, body { width: 848px; height: 1200px; overflow: hidden; }
  body {
    position: relative;
    font-family: "Roboto", Arial, sans-serif;
    color: var(--ink);
    background: linear-gradient(180deg, var(--sky-top) 0%, #7fb0cd 30%, var(--sky-mid) 55%, #5a9dbd 68%, var(--sky-bottom) 90%, #a6c6db 100%);
  }
  .shapes { position: absolute; left: 0; top: 0; }
  .block { position: absolute; }
  .title {
    left: 371px; top: 56px; width: 243px; height: 51px;
    color: var(--white); font-size: 40px; line-height: 51px; text-align: center; font-weight: 400;
  }
  .intro {
    left: 310px; top: 117px; width: 484px;
    font-size: 19.6px; line-height: 24px;
  }
  .intro .line { display: block; white-space: nowrap; text-align: justify; text-align-last: justify; }
  .tab-label { color: var(--white); font-size: 26px; line-height: 50px; font-weight: 400; }
  .highlights-label { left: 462px; top: 270px; width: 246px; text-align: center; }
  .highlights {
    left: 340px; top: 331px; width: 420px; list-style: none;
    font-size: 19.6px; line-height: 24px;
  }
  .highlights li { position: relative; padding-left: 40px; margin-bottom: 8px; }
  .highlights li::before { content: "•"; position: absolute; left: 3px; top: 0; }
  .overview-label { left: 90px; top: 490px; }
  .overview-label strong { font-weight: 700; }
  .overview {
    left: 64px; top: 547px; width: 460px;
    font-size: 19.6px; line-height: 24px; white-space: nowrap;
  }
  .overview .initial { color: #5d6e8c; }
  .range-label { left: 78px; top: 738px; }
  .range-backdrop {
    left: 42px; top: 793px; width: 767px; height: 301px; background: rgba(110,128,160,0.35);
  }
  .range {
    left: 47px; top: 793px; width: 756px; border-collapse: collapse;
    font-size: 19px; color: var(--white);
  }
  .range th, .range td { border: 1.5px solid #e9eef4; text-align: center; font-weight: 400; }
  .range th { background: var(--orange); height: 73px; line-height: 24px; }
  .range th small { display: block; font-size: 13px; line-height: 16px; }
  .range td { background: linear-gradient(180deg, #6f87a8, var(--slate-dark)); }
  .range td.model { font-size: 17px; }
  .range td.use { text-align: left; padding-left: 21px; line-height: 24px; }
  .range tr.r1 td { height: 98px; }
  .range tr.r2 td { height: 50px; }
  .range tr.r3 td { height: 75px; }
</style>
</head>
<body>
<svg class="shapes" width="848" height="1200" viewBox="0 0 848 1200">
  <defs>
    <linearGradient id="introBand" x1="0" x2="1">
      <stop offset="0" stop-color="#e08a2e"/>
      <stop offset="0.35" stop-color="#e2923c"/>
      <stop offset="1" stop-color="#c9a98a" stop-opacity="0.15"/>
    </linearGradient>
    <linearGradient id="highBand" x1="0" x2="1">
      <stop offset="0" stop-color="#7a8ba8"/>
      <stop offset="0.5" stop-color="#7589a7"/>
      <stop offset="1" stop-color="#7589a7" stop-opacity="0.2"/>
    </linearGradient>
    <linearGradient id="overBand" x1="0" x2="1">
      <stop offset="0" stop-color="#8796ad" stop-opacity="0.45"/>
      <stop offset="0.55" stop-color="#c69b66"/>
      <stop offset="1" stop-color="#e08a2e"/>
    </linearGradient>
    <linearGradient id="render" x1="0" x2="0" y1="0" y2="1">
      <stop offset="0" stop-color="#9fb6c8" stop-opacity="0.55"/>
      <stop offset="0.5" stop-color="#a7adb6" stop-opacity="0.6"/>
      <stop offset="1" stop-color="#8fb1c6" stop-opacity="0.4"/>
    </linearGradient>
    <linearGradient id="photoA" x1="0" x2="1" y1="0" y2="1">
      <stop offset="0" stop-color="#cfc9c2"/>
      <stop offset="1" stop-color="#4a3d36"/>
    </linearGradient>
    <linearGradient id="photoB" x1="0" x2="0" y1="0" y2="1">
      <stop offset="0" stop-color="#8ea7bd"/>
      <stop offset="1" stop-color="#8d7b68"/>
    </linearGradient>
    <linearGradient id="photoC" x1="0" x2="1" y1="0" y2="1">
      <stop offset="0" stop-color="#1e1e20"/>
      <stop offset="0.6" stop-color="#1f3f8a"/>
      <stop offset="1" stop-color="#151517"/>
    </linearGradient>
  </defs>

  <rect x="55" y="32" width="215" height="448" fill="url(#render)" role="img" aria-label="Product render of the ZORIL32 extruder"/>

  <polygon points="282,165 342,84 848,84 848,246 342,246" fill="url(#introBand)"/>
  <polygon points="371,56 593,56 614,107 392,107" fill="var(--slate)"/>

  <polygon points="282,374 345,295 848,295 848,462 345,462" fill="url(#highBand)"/>
  <polygon points="462,270 685,270 708,320 485,320" fill="var(--orange)"/>

  <polygon points="59,520 495,520 538,606 495,692 59,692" fill="url(#overBand)"/>
  <polygon points="59,541 79,490 470,490 450,541" fill="var(--slate)"/>

  <polygon points="52,788 72,738 328,738 308,788" fill="var(--slate)"/>

  <g role="img" aria-label="Photo of a technician assembling an extruder">
    <polygon points="500,513 545,425 633,425 678,513 633,601 545,601" fill="url(#photoA)" stroke="var(--hex-edge)" stroke-width="2"/>
  </g>
  <g role="img" aria-label="Photo of a large printed structural part in a workshop">
    <polygon points="636,605 681,517 769,517 814,605 769,693 681,693" fill="url(#photoB)" stroke="var(--hex-edge)" stroke-width="2"/>
  </g>
  <g role="img" aria-label="Technical drawing of a robot arm printing a tall lattice part">
    <polygon points="500,695 545,606 633,606 678,695 633,784 545,784" fill="url(#photoC)" stroke="var(--hex-edge)" stroke-width="2"/>
  </g>
</svg>

<h1 class="block title">ZORIL32</h1>
<p class="block intro">
  <span class="line">ZORIL32 features a 35 mm screw, 4 independent</span>
  <span class="line">heating zones, and a maximum extrusion temperature</span>
  <span class="line">of 450 °C. It delivers up to 40 kg/h (benchmarked with</span>
  <span class="line">PETG +30% GF) for reliable, repeatable output.</span>
</p>

<h2 class="block tab-label highlights-label">HIGHLIGHTS</h2>
<ul class="block highlights">
  <li>High-throughput system for heavyduty<br>production and large assemblies.</li>
  <li>Stable melt quality at high flow rates for<br>structural parts.</li>
</ul>

<h2 class="block tab-label overview-label"><strong>ZORIL SERIES</strong> OVERVIEW</h2>
<p class="block overview"><span class="initial">Z</span>ORIL extruders are designed for continuous,<br>high-throughput production of large-format<br>parts using reinforced thermoplastics. Each model<br>includes multi-zone heating, reinforced-polymer-<br>ready screw/barrel geometry, and interfaces for<br>seamless robotic integration.</p>

<h2 class="block tab-label range-label">PRODUCT RANGE</h2>
<div class="block range-backdrop"></div>
<table class="block range">
  <colgroup><col style="width:80px"><col style="width:97px"><col style="width:132px"><col style="width:91px"><col style="width:150px"><col style="width:206px"></colgroup>
  <tr>
    <th>Model</th><th>Screw<br>Diameter</th><th>Output<br>Capacity<small>(PETG +30% GF)</small></th><th>Heating<br>Zones</th><th>Maximum<br>Temperature</th><th>Primary Use Cases</th>
  </tr>
  <tr class="r1">
    <td class="model">ZORIL15</td><td>25 mm</td><td>15 kg/h</td><td>4</td><td>450 °C</td><td class="use">R&amp;D labs,<br>universities,<br>mid-size<br>prototypes</td>
  </tr>
  <tr class="r2">
    <td class="model">ZORIL20</td><td>25 mm</td><td>20 kg/h</td><td>4</td><td>450 °C</td><td class="use">Industrial prototyp-<br>ing, tooling &amp; molds</td>
  </tr>
  <tr class="r3">
    <td class="model">ZORIL32</td><td>35 mm</td><td>40 kg/h</td><td>4</td><td>450 °C</td><td class="use">Heavy-duty produc-<br>tion, large structural<br>parts</td>
  </tr>
</table>
</body>
</html>
```